The Lantern Circle

I need a design for a 1 page flyer but also a brochure

Target Market(s)

Wealthy, elegant, intelligent, discerning women who are on a journey of self-discovery.

Industry/Entity Type

Spiritual and personal development, yoga, meditation

Requirements
Must have
• Be very elegant, attractive, upmarket minimalist but also bit mystical
Nice to have
• I would like to use my logo (see uploaded file). The texts are also uploaded. One for the 1 page flyer 1 for a full brochure
Should not have
• be too busy, multicoloured, garish.

```html
<!DOCTYPE html>
<html lang="en">
<head>
<meta charset="utf-8">
<title>The Lantern Circle – Pathways to Our Inner Light</title>
<link rel="stylesheet" href="https://fonts.googleapis.com/css2?family=Poppins:wght@400;500;600&family=Advent+Pro:wght@300;400;600;700&family=Comfortaa:wght@500;600&display=swap">
<style>
:root{
  --green:#0f5a2c;
  --green-deep:#0a4420;
  --sage:#a9c3b0;
  --ink:#222;
  --grey:#6e6e6e;
  --stage:#b2b2b2;
  --paper:#ffffff;
}
*{margin:0;padding:0;box-sizing:border-box}
html,body{width:1200px;height:2566px;overflow:hidden}
body{background:var(--stage);font-family:'Poppins',sans-serif;color:var(--ink);position:relative}
.spread{position:absolute;left:104px;width:997px;height:705px;background:var(--paper);overflow:hidden}
.spread-cover{top:952px}
.spread-inner{top:1747px;height:704px}

/* brand lockup */
.brand{position:absolute;text-align:center;font-family:'Poppins',sans-serif;font-weight:400;color:var(--grey);font-size:12.5px;line-height:16px;letter-spacing:.5px}
.brand-dot{display:block;margin:0 auto 10px;width:34px;height:34px;border-radius:50%;background:var(--green)}

/* back cover */
.arch{position:absolute;left:108px;top:218px;width:285px;height:487px;border-radius:143px 143px 0 0;background:linear-gradient(180deg,#14683a 0%,var(--green) 45%,var(--green-deep) 100%);color:#fff;text-align:center}
.arch-title{position:absolute;top:58px;left:0;right:0;font-family:'Advent Pro',sans-serif;font-weight:400;font-size:16.5px;line-height:17px;letter-spacing:.3px}
.arch-text{position:absolute;top:100px;left:40px;right:40px;font-size:10.3px;line-height:12.6px}
.contact-icons{position:absolute;top:181px;left:0;right:0;display:flex;justify-content:center;gap:7px}
.contact-icons span{width:21px;height:21px;border-radius:50%;background:#e9efe9;display:flex;align-items:center;justify-content:center}
.contact-lines{position:absolute;top:220px;left:0;right:0;font-size:14px;line-height:25px;letter-spacing:.2px}
.still-life{position:absolute;left:76px;top:555px;width:335px;height:120px;border-radius:40px 40px 10px 10px;background:linear-gradient(90deg,#c9c9c6 0%,#e7e1d6 35%,#d98aa0 50%,#e8dcc8 70%,#cfcfcc 100%)}
.mandala-left{position:absolute;left:-40px;top:90px;width:190px;height:560px;border-radius:0 280px 280px 0;background:radial-gradient(ellipse at left center,#f4f4f4,#fafafa 70%,transparent 72%)}

/* front cover */
.figure{position:absolute;left:585px;top:135px;width:325px;height:340px;border-radius:50%;background:radial-gradient(circle at 50% 60%,var(--green) 0%,#2f7247 30%,#cfdcd3 55%,#f4f6f4 72%,transparent 73%)}
.title{position:absolute;left:600px;width:298px;text-align:center;color:var(--green-deep);font-family:'Advent Pro',sans-serif}
.t1{top:485px;font-weight:300;font-size:36px;line-height:36px;color:#2a2a2a;letter-spacing:.5px}
.t2{top:518px;font-weight:600;font-size:38px;line-height:38px;color:#1a3d26}
.t3{top:547px;font-weight:700;font-size:66px;line-height:66px;letter-spacing:.5px}
.place{position:absolute;left:659px;top:620px;width:179px;height:22px;border-radius:11px;background:#7a7a7a;color:#fff;font-size:15px;line-height:22px;text-align:center;letter-spacing:.4px}
.dates{position:absolute;left:600px;top:648px;width:298px;text-align:center;font-size:17px;letter-spacing:4px;color:#111}
.dates b{font-weight:600}

/* inner spread */
.lead{position:absolute;left:47px;top:44px;width:330px;font-size:13.5px;line-height:15px;color:#111}
.h{position:absolute;font-family:'Comfortaa',sans-serif;font-weight:600;color:var(--green);font-size:17.5px;letter-spacing:.2px;white-space:nowrap}
.body{position:absolute;font-size:9.6px;line-height:11.3px;color:#222}
.justify{text-align:justify}
.body p+p{margin-top:11px}
.path-item{position:absolute;display:flex;align-items:center;gap:9px;font-size:10.6px;line-height:12px;font-weight:500;color:#1a1a1a}
.path-icon{width:20px;height:20px;border-radius:50%;background:var(--green);flex:none;display:flex;align-items:center;justify-content:center}
.path-icon i{width:8px;height:8px;border-radius:50%;border:1.5px solid #fff;display:block}
.hold-band{position:absolute;left:0;top:496px;width:357px;height:154px;background:var(--green);border-radius:0 77px 77px 0}
.hold-text{position:absolute;left:47px;top:522px;width:250px;color:#fff;font-size:9.6px;line-height:11.3px;text-align:justify}
.photo-band{position:absolute;left:421px;top:496px;width:576px;height:154px;border-radius:77px 0 0 77px;background:linear-gradient(90deg,#1b2230 0%,#2c2a2a 45%,#4a3a2c 80%,#6b5236 100%)}
.photo-figure{position:absolute;left:796px;top:430px;width:150px;height:220px;border-radius:75px 75px 0 0;background:linear-gradient(180deg,rgba(70,60,50,.35),rgba(60,48,36,.8))}
.photo-ring{position:absolute;top:514px;width:114px;height:114px;border-radius:50%;border:6px solid var(--green);background:radial-gradient(circle,#c6c2b4 0%,#8c9a7a 60%,#5d6f50 100%)}
</style>
</head>
<body>

<section class="spread spread-cover">
  <div class="mandala-left" role="img" aria-label="Faint mandala ornament"></div>

  <div class="brand" style="left:176px;top:118px;width:150px">
    <span class="brand-dot"></span>THE LANTERN<br>CIRCLE
  </div>

  <div class="arch">
    <div class="arch-title">A JOURNEY THROUGH<br>THE INNER REALMS</div>
    <div class="arch-text">As these pathways weave together, a deeper journey unfolds—a movement from the surface of daily life into the quiet, spacious layers of the inner world</div>
    <div class="contact-icons">
      <span><svg width="12" height="12" viewBox="0 0 24 24"><path fill="#0f5a2c" d="M6.6 10.8c1.4 2.8 3.8 5.1 6.6 6.6l2.2-2.2c.3-.3.7-.4 1-.2 1.1.4 2.3.6 3.6.6.6 0 1 .4 1 1V20c0 .6-.4 1-1 1C10.6 21 3 13.4 3 4c0-.6.4-1 1-1h3.5c.6 0 1 .4 1 1 0 1.3.2 2.5.6 3.6.1.3 0 .7-.2 1z"/></svg></span>
      <span><svg width="12" height="12" viewBox="0 0 24 24"><path fill="#0f5a2c" d="M3 5h18v14H3z"/><path fill="none" stroke="#fff" stroke-width="2" d="M3 6l9 7 9-7"/></svg></span>
      <span><svg width="12" height="12" viewBox="0 0 24 24"><circle cx="12" cy="12" r="9" fill="none" stroke="#0f5a2c" stroke-width="2"/><path fill="none" stroke="#0f5a2c" stroke-width="1.6" d="M3 12h18M12 3c3 3 3 15 0 18M12 3c-3 3-3 15 0 18"/></svg></span>
    </div>
    <div class="contact-lines">+41 79 000 48 15<br>mara@the-lantern-circle.com<br>www.the-lantern-circle.com</div>
  </div>
  <div class="still-life" role="img" aria-label="Spa still life with stacked stones, pink orchid, towel and candles"></div>

  <div class="brand" style="left:673px;top:50px;width:150px">
    <span class="brand-dot"></span>THE LANTERN<br>CIRCLE
  </div>
  <div class="figure" role="img" aria-label="Silhouette of a woman meditating in lotus pose before a faint mandala"></div>
  <div class="title t1">PATHWAYS TO</div>
  <div class="title t2">OUR INNER</div>
  <div class="title t3">LIGHT</div>
  <div class="place">Valdorra, Italy</div>
  <div class="dates"><b>12–16</b> May 2026</div>
</section>

<section class="spread spread-inner">
  <p class="lead">Within the quiet of your being, your inner light waits to be remembered.</p>

  <h2 class="h" style="left:47px;top:88px">Why I Created This Retreat</h2>
  <div class="body justify" style="left:47px;top:114px;width:405px">
    <p>My relationship with yoga began in 1997, while I was working with the World Concord Council in Rome. To be honest, I hated it at first. My body was stiff, tense, and unfamiliar to me. The practice felt uncomfortable—an almost psycho-physical irritation I couldn’t quite explain. And yet, something was shifting. A colleague commented, “You’re so much nicer when you come back from yoga,” and I began to notice moments of awareness I had never experienced before—my toes, the palms of my hands, a single muscle along my back. Something inside me was waking up. Years later, as I transitioned out of an intense, travel-heavy career and trained for the Lakeshore Marathon, yoga resurfaced—not as stretching, but as stillness.</p>
    <p>Though I still couldn’t touch my toes, I realised that an hour on the mat quieted my mind more deeply than 26.2 miles of running ever could. The penny dropped. Yoga wasn’t simply physical; it was one doorway inward. They say, “You will find yourself on your mat,” and that was becoming true. I stepped into my first teacher training, not to teach, but to understand. It felt less like entering a new world and more like returning to an original one. Fast-forward through years of practice, curiosity, study, and exploration, and I have come to understand something essential: there is no single path. Dogma has no place in self-discovery. Each of us is unique, and each of us will resonate with different tools at different moments in our lives.</p>
    <p>What supports us today may shift tomorrow. This is not only natural—it is to be honoured. This retreat is rooted in that philosophy. It is not a yoga retreat, though yoga is one of the practices we draw from. Instead, it is a discerning, intelligent, and elegant container for gentle yet deep inner work. My intention is to offer a constellation of modalities—movement, breath, meditation, somatics, energy practices, craftwork, nature immersion—so you may discover what truly serves you. The group remains intentionally small so that each person receives the attention, guidance, and individualisation they need. This is an invitation to step toward your inner light, in your own way, at your own rhythm.</p>
  </div>

  <h2 class="h" style="left:544px;top:40px">The Lantern Approach</h2>
  <div class="body" style="left:544px;top:70px;width:185px">My approach is grounded in the understanding that self-discovery is not linear and not prescriptive. We each arrive with different histories, patterns, and sensitivities, and therefore no single modality can speak to everyone in the same way. I work by offering a curated selection of practices—movement, breath, somatics, meditation, energetic work, and creative exploration—so you can experience what truly resonates for you. I invite each person to explore with curiosity rather than expectation, allowing space for insight, release, or stillness to arise naturally. My intention is to guide with clarity while honouring your autonomy and inner wisdom.</div>

  <h2 class="h" style="left:774px;top:40px">About Me</h2>
  <div class="body" style="left:774px;top:70px;width:190px">I am an Ashtanga practitioner who teaches various styles of yoga—dynamic, hatha, yin, nidra—with a somatic and intuitive approach. I teach meditation, breathwork, and energy practices, and I am an RYT-500hr teacher certified in advanced pranayama and meditation. I have been an GCA Certified Coach for over 10 years. My earlier career spanned international development with the European Policy Office, INGOs, the World Concord Council, and my own consultancy focused on creating inclusive organisations. These experiences shaped my ability to listen deeply, hold space, and support transformation with clarity and compassion.</div>

  <h2 class="h" style="left:544px;top:308px">Pathways We Will Explore</h2>
  <div class="path-item" style="left:544px;top:348px"><span class="path-icon"><i></i></span>Evolove<br>Your Energy</div>
  <div class="path-item" style="left:544px;top:384px"><span class="path-icon"><i></i></span>Immerse in<br>Frequency</div>
  <div class="path-item" style="left:544px;top:422px"><span class="path-icon"><i></i></span>Harness<br>Your Breath</div>
  <div class="path-item" style="left:696px;top:348px"><span class="path-icon"><i></i></span>Embodied<br>Awakening</div>
  <div class="path-item" style="left:696px;top:384px"><span class="path-icon"><i></i></span>Shadow<br>Exploration</div>
  <div class="path-item" style="left:696px;top:422px"><span class="path-icon"><i></i></span>Reiki<br>Healing</div>
  <div class="path-item" style="left:829px;top:348px"><span class="path-icon"><i></i></span>Forest<br>Bathing</div>
  <div class="path-item" style="left:829px;top:384px"><span class="path-icon"><i></i></span>Centering at<br>Your Fingertips</div>

  <h2 class="h" style="left:47px;top:466px">How I Hold Space</h2>
  <div class="hold-band"></div>
  <p class="hold-text">I have cultivated a quiet, practiced intuition that allows me to meet people exactly where they are. Through energy work, meditation, and somatics, I’ve learned to sense subtle shifts within a room or within an individual. This attunement shows me when to guide, when to soften, and when to simply allow — and when needed, when to be clear and firm. I am able to hold people gently yet accountably, ensuring they do not slip away from the very work they came to meet.</p>

  <div class="photo-band" role="img" aria-label="Dusk mountain landscape backdrop"></div>
  <div class="photo-figure" role="img" aria-label="Silhouette of a woman in tree pose at sunset"></div>
  <div class="photo-ring" style="left:437px" role="img" aria-label="Woman meditating on grass"></div>
  <div class="photo-ring" style="left:565px" role="img" aria-label="Man splashing water in a lake"></div>
  <div class="photo-ring" style="left:691px" role="img" aria-label="Person receiving a relaxing energy treatment"></div>
</section>

</body>
</html>
```